Billiards 50th Anniversary Calendar

Need a custom calendar designed to finish at 8.5 x 11. and to be supplied as a pdf print file including .25 bleed on all sides. Total is 24 pages. I will supply one image per calendar month. Cover to have a collage of monthly images or samples of some of your favorites incorporated with a cool design that transitions throughout the calendar. The client's 50th Anniversary logo must be incorporated into the design.

Back cover has a group image to be incorporated as well.

Target Market(s)

Calendar is selling to their billiard clients

Industry/Entity Type

Male dominant industry

Requirements
Must have
• Must have a design element that continues through the calendar but flows with the images well. One image per calendar month.

```html
<!DOCTYPE html>
<html lang="en">
<head>
<meta charset="utf-8">
<title>Rackline Billiards 50th Anniversary Calendar</title>
<link href="https://fonts.googleapis.com/css2?family=Jost:wght@300;400;500&display=swap" rel="stylesheet">
<style>
  :root{
    --backdrop:#ebe7e1;
    --paper:#ffffff;
    --green:#1f9a4a;
    --orange:#f0821e;
    --sunday:#b3262d;
    --chip:#ededed;
    --ink:#333333;
    --year:#b9b9b9;
    --label:#8a8a8a;
  }
  *{box-sizing:border-box;margin:0;padding:0}
  html,body{width:1200px;height:923px;overflow:hidden}
  body{background:var(--backdrop);font-family:"Jost",sans-serif;position:relative;color:var(--ink)}

  .month-page{position:absolute;width:258px;height:398px;background:var(--paper);box-shadow:0 2px 6px rgba(0,0,0,.18)}
  .month-photo{height:199px;width:100%}
  .month-sheet{position:relative;height:199px}
  .month-title{position:absolute;top:17px;left:0;width:100%;text-align:center;font-size:16px;font-weight:400;letter-spacing:-.2px}
  .month-title .year{color:var(--year);font-weight:300}
  .brand-mark{position:absolute;top:14px;right:10px;display:flex;align-items:center;gap:2px;font-size:5.5px;font-weight:500;color:var(--green);line-height:1}
  .brand-mark .dot{width:6px;height:6px;border-radius:50%;background:var(--orange)}
  .weekdays,.days{position:absolute;left:26px;display:grid;grid-template-columns:repeat(7,29px)}
  .weekdays{top:48px}
  .weekdays span{font-size:3.6px;font-weight:500;text-align:center;color:var(--label);letter-spacing:.1px}
  .weekdays span:first-child{color:var(--sunday)}
  .days{top:55px;grid-auto-rows:27.5px}
  .day{width:22px;height:22px;margin:0 auto;border-radius:50%;background:var(--chip);display:flex;align-items:center;justify-content:center;font-size:11px;font-weight:400}
  .day.sun{background:var(--sunday);color:#fff}
  .day.pair{position:relative;font-size:8.5px}
  .day.pair i{position:absolute;font-style:normal}
  .day.pair i:first-child{top:2px;left:2px}
  .day.pair i:last-child{bottom:1px;right:2px}
  .start-2{grid-column-start:2}.start-3{grid-column-start:3}.start-5{grid-column-start:5}
  .start-6{grid-column-start:6}.start-7{grid-column-start:7}
  .band{position:absolute;left:0;bottom:0;width:100%;height:8px}
  .band.green{background:var(--green)} .band.orange{background:var(--orange)}
  .green-text{color:var(--green)} .orange-text{color:var(--orange)}

  .col-1{left:55px}.col-2{left:332px}.col-3{left:609px}
  .row-1{top:50px}.row-2{top:475px}

  .back-cover{position:absolute;left:886px;top:674px;width:258px;height:199px;background:linear-gradient(180deg,#2a1e1c 0%,#4a2a22 45%,#a5521f 80%,#e07a25 100%);box-shadow:0 2px 6px rgba(0,0,0,.18)}
  .back-cover .cover-brand{position:absolute;left:0;right:0;bottom:22px;display:flex;justify-content:center;align-items:center;gap:3px;font-size:9px;font-weight:500;color:#f6d34a}
  .back-cover .cover-brand .dot{width:8px;height:8px;border-radius:50%;background:var(--green)}
</style>
</head>
<body>

<!-- July -->
<section class="month-page col-1 row-1">
  <div class="month-photo" role="img" aria-label="Pin-up model in floral dress reclining on a blue pool table" style="background:linear-gradient(135deg,#1c2a2c 0%,#2f3f52 40%,#2d83a8 75%,#4aa7c9 100%)"></div>
  <div class="month-sheet">
    <h2 class="month-title"><span class="green-text">JULY</span><span class="year">2022</span></h2>
    <div class="brand-mark"><span class="dot"></span>RACKLINE</div>
    <div class="weekdays"><span>SUNDAY</span><span>MONDAY</span><span>TUESDAY</span><span>WEDNESDAY</span><span>THURSDAY</span><span>FRIDAY</span><span>SATURDAY</span></div>
    <div class="days">
      <span class="day start-6">1</span><span class="day">2</span>
      <span class="day sun">3</span><span class="day">4</span><span class="day">5</span><span class="day">6</span><span class="day">7</span><span class="day">8</span><span class="day">9</span>
      <span class="day sun">10</span><span class="day">11</span><span class="day">12</span><span class="day">13</span><span class="day">14</span><span class="day">15</span><span class="day">16</span>
      <span class="day sun">17</span><span class="day">18</span><span class="day">19</span><span class="day">20</span><span class="day">21</span><span class="day">22</span><span class="day">23</span>
      <span class="day sun pair"><i>24</i><i>31</i></span><span class="day">25</span><span class="day">26</span><span class="day">27</span><span class="day">28</span><span class="day">29</span><span class="day">30</span>
    </div>
    <div class="band orange"></div>
  </div>
</section>

<!-- August -->
<section class="month-page col-2 row-1">
  <div class="month-photo" role="img" aria-label="Pin-up model in red dress seated on a pool table holding a cue" style="background:linear-gradient(180deg,#141414 0%,#2a1618 45%,#8a1d22 65%,#2b8fc2 100%)"></div>
  <div class="month-sheet">
    <h2 class="month-title"><span class="orange-text">AUGUST</span><span class="year">2022</span></h2>
    <div class="brand-mark"><span class="dot"></span>RACKLINE</div>
    <div class="weekdays"><span>SUNDAY</span><span>MONDAY</span><span>TUESDAY</span><span>WEDNESDAY</span><span>THURSDAY</span><span>FRIDAY</span><span>SATURDAY</span></div>
    <div class="days">
      <span class="day start-2">1</span><span class="day">2</span><span class="day">3</span><span class="day">4</span><span class="day">5</span><span class="day">6</span>
      <span class="day sun">7</span><span class="day">8</span><span class="day">9</span><span class="day">10</span><span class="day">11</span><span class="day">12</span><span class="day">13</span>
      <span class="day sun">14</span><span class="day">15</span><span class="day">16</span><span class="day">17</span><span class="day">18</span><span class="day">19</span><span class="day">20</span>
      <span class="day sun">21</span><span class="day">22</span><span class="day">23</span><span class="day">24</span><span class="day">25</span><span class="day">26</span><span class="day">27</span>
      <span class="day sun">28</span><span class="day">29</span><span class="day">30</span><span class="day">31</span>
    </div>
    <div class="band green"></div>
  </div>
</section>

<!-- September -->
<section class="month-page col-3 row-1">
  <div class="month-photo" role="img" aria-label="Pin-up model in polka-dot rose dress reclining on a counter before a brick wall" style="background:linear-gradient(160deg,#8a4a3c 0%,#6e3a30 40%,#b09a80 70%,#d9c3a4 100%)"></div>
  <div class="month-sheet">
    <h2 class="month-title"><span class="green-text">SEPTEMBER</span><span class="year">2022</span></h2>
    <div class="brand-mark"><span class="dot"></span>RACKLINE</div>
    <div class="weekdays"><span>SUNDAY</span><span>MONDAY</span><span>TUESDAY</span><span>WEDNESDAY</span><span>THURSDAY</span><span>FRIDAY</span><span>SATURDAY</span></div>
    <div class="days">
      <span class="day start-5">1</span><span class="day">2</span><span class="day">3</span>
      <span class="day sun">4</span><span class="day">5</span><span class="day">6</span><span class="day">7</span><span class="day">8</span><span class="day">9</span><span class="day">10</span>
      <span class="day sun">11</span><span class="day">12</span><span class="day">13</span><span class="day">14</span><span class="day">15</span><span class="day">16</span><span class="day">17</span>
      <span class="day sun">18</span><span class="day">19</span><span class="day">20</span><span class="day">21</span><span class="day">22</span><span class="day">23</span><span class="day">24</span>
      <span class="day sun">25</span><span class="day">26</span><span class="day">27</span><span class="day">28</span><span class="day">29</span><span class="day">30</span>
    </div>
    <div class="band orange"></div>
  </div>
</section>

<!-- October -->
<section class="month-page col-1 row-2">
  <div class="month-photo" role="img" aria-label="Pin-up model in black floral dress lying across a blue pool table with balls" style="background:linear-gradient(135deg,#1f86b8 0%,#2aa3d6 45%,#1c2430 70%,#2196c9 100%)"></div>
  <div class="month-sheet">
    <h2 class="month-title"><span class="orange-text">OCTOBER</span><span class="year">2022</span></h2>
    <div class="brand-mark"><span class="dot"></span>RACKLINE</div>
    <div class="weekdays"><span>SUNDAY</span><span>MONDAY</span><span>TUESDAY</span><span>WEDNESDAY</span><span>THURSDAY</span><span>FRIDAY</span><span>SATURDAY</span></div>
    <div class="days">
      <span class="day start-7">1</span>
      <span class="day sun">2</span><span class="day">3</span><span class="day">4</span><span class="day">5</span><span class="day">6</span><span class="day">7</span><span class="day">8</span>
      <span class="day sun">9</span><span class="day">10</span><span class="day">11</span><span class="day">12</span><span class="day">13</span><span class="day">14</span><span class="day">15</span>
      <span class="day sun">16</span><span class="day">17</span><span class="day">18</span><span class="day">19</span><span class="day">20</span><span class="day">21</span><span class="day">22</span>
      <span class="day sun pair"><i>23</i><i>30</i></span><span class="day pair"><i>24</i><i>31</i></span><span class="day">25</span><span class="day">26</span><span class="day">27</span><span class="day">28</span><span class="day">29</span>
    </div>
    <div class="band green"></div>
  </div>
</section>

<!-- November -->
<section class="month-page col-2 row-2">
  <div class="month-photo" role="img" aria-label="Pin-up model lying on a pool table resting her chin on her hand" style="background:linear-gradient(180deg,#121212 0%,#1e1c1c 50%,#2b8fc2 78%,#4a2a20 100%)"></div>
  <div class="month-sheet">
    <h2 class="month-title"><span class="green-text">NOVEMBER</span><span class="year">2022</span></h2>
    <div class="brand-mark"><span class="dot"></span>RACKLINE</div>
    <div class="weekdays"><span>SUNDAY</span><span>MONDAY</span><span>TUESDAY</span><span>WEDNESDAY</span><span>THURSDAY</span><span>FRIDAY</span><span>SATURDAY</span></div>
    <div class="days">
      <span class="day start-3">1</span><span class="day">2</span><span class="day">3</span><span class="day">4</span><span class="day">5</span>
      <span class="day sun">6</span><span class="day">7</span><span class="day">8</span><span class="day">9</span><span class="day">10</span><span class="day">11</span><span class="day">12</span>
      <span class="day sun">13</span><span class="day">14</span><span class="day">15</span><span class="day">16</span><span class="day">17</span><span class="day">18</span><span class="day">19</span>
      <span class="day sun">20</span><span class="day">21</span><span class="day">22</span><span class="day">23</span><span class="day">24</span><span class="day">25</span><span class="day">26</span>
      <span class="day sun">27</span><span class="day">28</span><span class="day">29</span><span class="day">30</span>
    </div>
    <div class="band orange"></div>
  </div>
</section>

<!-- December -->
<section class="month-page col-3 row-2">
  <div class="month-photo" role="img" aria-label="Flapper-style model in sheer robe seated on a pool table" style="background:linear-gradient(180deg,#0f0f0f 0%,#1f1c1a 45%,#cdbfae 65%,#2a8ec2 100%)"></div>
  <div class="month-sheet">
    <h2 class="month-title"><span class="orange-text">DECEMBER</span><span class="year">2022</span></h2>
    <div class="brand-mark"><span class="dot"></span>RACKLINE</div>
    <div class="weekdays"><span>SUNDAY</span><span>MONDAY</span><span>TUESDAY</span><span>WEDNESDAY</span><span>THURSDAY</span><span>FRIDAY</span><span>SATURDAY</span></div>
    <div class="days">
      <span class="day start-5">1</span><span class="day">2</span><span class="day">3</span>
      <span class="day sun">4</span><span class="day">5</span><span class="day">6</span><span class="day">7</span><span class="day">8</span><span class="day">9</span><span class="day">10</span>
      <span class="day sun">11</span><span class="day">12</span><span class="day">13</span><span class="day">14</span><span class="day">15</span><span class="day">16</span><span class="day">17</span>
      <span class="day sun">18</span><span class="day">19</span><span class="day">20</span><span class="day">21</span><span class="day">22</span><span class="day">23</span><span class="day">24</span>
      <span class="day sun">25</span><span class="day">26</span><span class="day">27</span><span class="day">28</span><span class="day">29</span><span class="day">30</span><span class="day">31</span>
    </div>
    <div class="band green"></div>
  </div>
</section>

<!-- Back cover -->
<section class="back-cover" role="img" aria-label="Group photo of all calendar models posing together at the bar">
  <div class="cover-brand"><span class="dot"></span>RACKLINE BILLIARDS</div>
</section>

</body>
</html>
```